Good afternoon,
1. Can we also have the ‘Lanternbugs selections of the month’ moved to the left side and smaller than the logo quote ‘inquisitive minds on adventure’ as it’s just a subheading. That said can we have the ‘Inquisitive minds on adventure’ a little larger.
2. Can we have the order of the drop down menus as. Age then Theme then Location (no price). Next to these titles can we have a small image such as a locator point next to ‘location’, two people holding hands adult and child net to ‘age’ and something adventure/city next to ‘theme’, an image to represent the drop down menus. See below:

3. Can we please use this as a logo instead of what we have at the moment. And the same type of setup as what I have here. I really like this map of Australia. We have the rights to it and I have attached it as a file for you to use.

4. Can the selection buttons all be the same blue as the blue in the logo please. Can every part of the page have the logo blue/dirty orange also? Makes it calmer.

5. Could you please add a ‘calendar’ to the tabs (in blue at the top of the page, on the left of ‘add and activity’ .
Let me know how you go. Thanks

Target Market(s)

• Parents and care-givers
• Teachers
• Children (child-friendly)
• Customers are those who ask the question ‘what am I going to do with my child/ren this week/weekend/month’

Industry/Entity Type

Quote

Number of Pages Required

4 page

Font styles to use
Sans Serif

Requirements
Must have
• An ecommerce website (platform) with a responsive system for IOS and Android
• Easy to navigate, user-friendly clean
Nice to have
• some interactive maps
Should not have
• To much clutter/info

```html
<!DOCTYPE html>
<html lang="en">
<head>
<meta charset="utf-8">
<title>Lanternbugs Melbourne</title>
<link rel="stylesheet" href="https://fonts.googleapis.com/css2?family=Catamaran:wght@500;600;700&family=Open+Sans:wght@400;600;700&family=Zilla+Slab:wght@500&display=swap">
<style>
:root{
  --orange:#f7941d;
  --orange-dark:#e07412;
  --blue:#0d4ea6;
  --ink:#1c1c1c;
  --text:#555;
  --page:#f1f1f1;
  --footer:#2a2a2a;
  --footer-bar:#161616;
  --footer-text:#dddddd;
  --white:#fff;
}
*{box-sizing:border-box;margin:0;padding:0}
html,body{width:1200px;height:2456px;overflow:hidden}
body{position:relative;background:var(--page);font-family:"Open Sans",sans-serif;color:var(--text)}
.abs{position:absolute}
.heading{font-family:"Catamaran",sans-serif;color:var(--ink)}

/* header */
.site-header{left:0;top:0;width:1200px;height:116px;background:var(--white)}
.brand{left:62px;top:26px;display:flex;align-items:center;gap:10px}
.brand-dot{width:26px;height:26px;border-radius:50%;background:var(--orange)}
.brand-name{font-family:"Catamaran",sans-serif;font-weight:700;font-size:40px;line-height:1;color:#3a3a3a}
.brand-city{left:258px;top:66px;font-family:"Catamaran",sans-serif;font-weight:600;font-size:19px;color:#8a8a8a}
.nav a{position:absolute;top:36px;height:38px;line-height:38px;font-family:"Catamaran",sans-serif;font-weight:600;font-size:17px;color:var(--ink);text-decoration:none;white-space:nowrap}
.nav .active{left:478px;width:72px;text-align:center;background:var(--orange);color:var(--white)}
.nav .tab-calendar{left:734px;width:92px;text-align:center;background:var(--blue);color:var(--white)}
.nav-search{left:1098px;top:33px;width:42px;height:41px;background:var(--ink);display:flex;align-items:center;justify-content:center}

/* hero */
.hero{left:0;top:116px;width:1200px;height:347px;background:linear-gradient(100deg,#d9c9b4 0%,#cfdbe2 22%,#e8e2d6 45%,#d7c1a8 62%,#c9d9e3 80%,#e5d6c2 100%)}
.hero-fade{left:0;top:116px;width:1200px;height:347px;background:linear-gradient(180deg,rgba(255,255,255,.55),rgba(255,255,255,.25) 60%,rgba(240,140,60,.25))}
.hero-title{left:0;top:184px;width:1200px;text-align:center;font-weight:600;font-size:48px;line-height:1.1}
.hero-sub{left:0;top:240px;width:1200px;text-align:center;font-family:"Catamaran",sans-serif;font-weight:500;font-size:22px;color:var(--ink)}
.search-panel{left:152px;top:300px;width:889px;height:95px;background:rgba(30,30,30,.88)}
.select{top:326px;width:221px;height:46px;background:var(--white);border-radius:2px;display:flex;align-items:center;padding:0 14px;gap:10px;font-size:15px;color:#9a9a9a}
.select .caret{margin-left:auto}
.btn-suggest{left:876px;top:322px;width:144px;height:46px;background:var(--blue);color:var(--white);font-family:"Catamaran",sans-serif;font-weight:700;font-size:20px;display:flex;align-items:center;justify-content:center;border-radius:2px}

/* main panel */
.main-panel{left:61px;top:463px;width:1080px;height:1632px;background:var(--white)}
.quick-btn{top:493px;height:50px;display:flex;align-items:center;justify-content:center;gap:8px;color:var(--white);font-family:"Catamaran",sans-serif;font-weight:700;font-size:17px;background:var(--blue)}

.section-title{left:90px;top:584px;font-weight:600;font-size:31px}
.slider-arrow{top:584px;width:36px;height:33px;background:var(--blue);display:flex;align-items:center;justify-content:center}

.theme-card{width:222px}
.theme-photo{width:222px;height:197px;border:1px solid #ddd}
.theme-card h3{margin-top:26px;font-family:"Catamaran",sans-serif;font-weight:600;font-size:18px;color:var(--ink)}
.theme-card p{margin-top:4px;font-size:12px;line-height:17px}
.read-more{display:inline-block;margin-top:7px;font-size:13px;color:var(--orange-dark);text-decoration:underline}

.newsletter{left:815px;top:493px;width:293px;height:227px;background:var(--blue);color:var(--white);padding:16px 28px}
.newsletter h2{font-family:"Zilla Slab",serif;font-weight:500;font-size:27px;text-align:center}
.newsletter p{font-size:13px;line-height:18px;text-align:center;margin-top:6px}
.newsletter .field{margin-top:18px;width:238px;height:42px;background:var(--white)}
.newsletter .submit{margin-top:10px;width:88px;height:38px;background:var(--orange);font-family:"Catamaran",sans-serif;font-weight:700;font-size:18px;display:flex;align-items:center;justify-content:center}
.promo{left:815px;top:758px;width:293px;height:414px;background:radial-gradient(circle at 50% 55%,#7bc043,#3c9a35 70%,#2f7f2c);border:1px solid #ddd}

/* lists */
.col-head{top:1339px;height:44px;display:flex;align-items:center;gap:10px;padding-left:8px;color:var(--white);font-family:"Catamaran",sans-serif;font-weight:600;font-size:19px}
.col-head.small{font-size:17px}
.col-head .ring{width:28px;height:28px;border-radius:50%;background:var(--white);display:flex;align-items:center;justify-content:center}
.suggest-item{left:90px;width:432px;height:128px;border:1px solid #e2e2e2;display:flex;padding:2px}
.suggest-item .thumb{width:185px;height:122px;flex:none}
.suggest-item .body{padding:6px 0 0 15px}
.suggest-item h4{font-family:"Catamaran",sans-serif;font-weight:600;font-size:16px;line-height:19px;color:var(--ink)}
.suggest-item p{font-size:11px;line-height:16px;margin-top:4px}
.suggest-item .read-more{margin-top:0;font-size:12px}
.post-card{left:537px;top:1387px;width:285px;height:388px;border:1px solid #e2e2e2;text-align:center}
.post-card .photo{height:181px}
.post-card h4{margin-top:32px;font-family:"Catamaran",sans-serif;font-weight:600;font-size:17px;color:var(--ink)}
.post-card p{margin:14px 28px 0;font-size:12px;line-height:18px}
.post-card .btn{margin:18px auto 0;width:114px;height:38px;background:var(--blue);color:var(--white);font-size:14px;display:flex;align-items:center;justify-content:center}
.feature-item{left:837px;width:270px;display:flex;gap:14px}
.feature-item .thumb{width:124px;height:86px;flex:none;border:2px solid #eee}
.feature-item p{font-size:11px;line-height:17px}
.feature-item b{color:var(--ink)}

/* footer */
.footer{left:0;top:2095px;width:1200px;height:318px;background:var(--footer)}
.footer-bar{left:0;top:2413px;width:1200px;height:43px;background:var(--footer-bar);color:#bbb;font-size:12px;display:flex;align-items:center;justify-content:center}
.f-title{top:2145px;font-family:"Catamaran",sans-serif;font-weight:500;font-size:25px;color:var(--white)}
.f-rule{top:2181px;width:52px;height:3px;background:var(--white)}
.f-line{font-size:13px;display:flex;align-items:center;gap:12px;color:var(--footer-text)}
.f-list{font-size:13px;line-height:23.3px;list-style:none;color:var(--footer-text)}
.f-list.bullets li::before{content:"";display:inline-block;width:5px;height:5px;border-radius:50%;background:var(--footer-text);margin:0 10px 2px 6px}
.social{top:2298px;width:30px;height:30px;border-radius:50%;background:#7a7a7a}
.map{left:869px;top:2215px;width:255px;height:164px;background:linear-gradient(135deg,#eef0e6,#dfe6d4 40%,#e9e4d6 70%,#cfdce6)}
</style>
</head>
<body>

<header class="abs site-header">
  <div class="abs brand"><span class="brand-dot"></span><span class="brand-name">Lanternbugs</span></div>
  <div class="abs brand-city">Melbourne</div>
  <nav class="nav">
    <a class="active" href="#">Home</a>
    <a href="#" style="left:564px">Featured adventures</a>
    <a class="tab-calendar" href="#">Calendar</a>
    <a href="#" style="left:840px">List an activity</a>
    <a href="#" style="left:980px">Destination</a>
  </nav>
  <div class="abs nav-search"><svg width="22" height="22" viewBox="0 0 22 22"><circle cx="9" cy="9" r="6.5" fill="none" stroke="#fff" stroke-width="2.6"/><line x1="14" y1="14" x2="20" y2="20" stroke="#fff" stroke-width="3" stroke-linecap="round"/></svg></div>
</header>

<section>
  <div class="abs hero" role="img" aria-label="Photo of children kayaking on a lake in life jackets"></div>
  <div class="abs hero-fade"></div>
  <h1 class="abs heading hero-title">Inquisitive minds on Adventure</h1>
  <p class="abs hero-sub">Specific support services for parents and carers are included here</p>
  <div class="abs search-panel"></div>
  <div class="abs select" style="left:172px">
    <svg width="24" height="20" viewBox="0 0 24 20"><circle cx="6" cy="3" r="2.8" fill="#aaa"/><path d="M2 20V9c0-2 2-3 4-3s4 1 4 3v11z" fill="#aaa"/><circle cx="18" cy="9" r="2.2" fill="#aaa"/><path d="M15 20v-6c0-1.5 1.4-2.4 3-2.4s3 .9 3 2.4v6z" fill="#aaa"/><path d="M10 12h5" stroke="#aaa" stroke-width="1.8"/></svg>Age
    <svg class="caret" width="12" height="8" viewBox="0 0 12 8"><path d="M0 0h12L6 8z" fill="#888"/></svg></div>
  <div class="abs select" style="left:406px">
    <svg width="22" height="20" viewBox="0 0 22 20"><rect x="1" y="8" width="6" height="12" fill="#aaa"/><rect x="8" y="2" width="6" height="18" fill="#aaa"/><rect x="15" y="11" width="6" height="9" fill="#aaa"/><path d="M11 0v2" stroke="#aaa" stroke-width="1.5"/></svg>Theme
    <svg class="caret" width="12" height="8" viewBox="0 0 12 8"><path d="M0 0h12L6 8z" fill="#888"/></svg></div>
  <div class="abs select" style="left:642px">
    <svg width="14" height="20" viewBox="0 0 14 20"><path d="M7 0C3 0 0 3 0 7c0 5 7 13 7 13s7-8 7-13c0-4-3-7-7-7z" fill="#aaa"/><circle cx="7" cy="7" r="2.6" fill="#fff"/></svg>Location
    <svg class="caret" width="12" height="8" viewBox="0 0 12 8"><path d="M0 0h12L6 8z" fill="#888"/></svg></div>
  <div class="abs btn-suggest">Suggestions</div>
</section>

<main>
  <div class="abs main-panel"></div>

  <div class="abs quick-btn" style="left:90px;width:226px">
    <svg width="18" height="20" viewBox="0 0 18 20"><circle cx="9" cy="9" r="8" fill="none" stroke="#fff" stroke-width="2"/><path d="M5 9l3 3 5-6" stroke="#fff" stroke-width="2" fill="none"/></svg>See your Suggestions</div>
  <div class="abs quick-btn" style="left:321px;width:224px">
    <svg width="18" height="20" viewBox="0 0 18 20"><circle cx="9" cy="5" r="4.5" fill="#fff"/><path d="M0 20c0-6 4-9 9-9s9 3 9 9z" fill="#fff"/></svg>Signup/Login</div>
  <div class="abs quick-btn" style="left:552px;width:226px">
    <svg width="18" height="18" viewBox="0 0 18 18"><path d="M18 0L0 8l8 2 2 8z" fill="#fff"/></svg>All Destinations</div>

  <h2 class="abs heading section-title">Explore by Theme</h2>
  <div class="abs slider-arrow" style="left:699px"><svg width="18" height="12" viewBox="0 0 18 12"><path d="M18 6H3M7 1L2 6l5 5" stroke="#fff" stroke-width="2" fill="none"/></svg></div>
  <div class="abs slider-arrow" style="left:740px"><svg width="18" height="12" viewBox="0 0 18 12"><path d="M0 6h15M11 1l5 5-5 5" stroke="#fff" stroke-width="2" fill="none"/></svg></div>

  <article class="abs theme-card" style="left:90px;top:643px">
    <div class="theme-photo" role="img" aria-label="Photo of a gallery room hung with framed paintings" style="background:linear-gradient(160deg,#4a3a2a,#8b6a42 55%,#c49a60)"></div>
    <h3>Explore Arts</h3><p>Lorem Ipsum is simply dummy text of the printing and typesetting industry.</p><a class="read-more" href="#">Read More</a>
  </article>
  <article class="abs theme-card" style="left:324px;top:643px">
    <div class="theme-photo" role="img" aria-label="Photo of a child looking up at a tall city building against the sky" style="background:linear-gradient(160deg,#1f3e74,#4f7fb8 50%,#9ab6d6)"></div>
    <h3>Explore Icons</h3><p>Lorem Ipsum is simply dummy text of the printing and typesetting industry.</p><a class="read-more" href="#">Read More</a>
  </article>
  <article class="abs theme-card" style="left:555px;top:643px">
    <div class="theme-photo" role="img" aria-label="Photo of a museum wall covered in historic passports" style="background:linear-gradient(160deg,#3b2230,#7a2f3b 50%,#5a4a6a)"></div>
    <h3>Explore History</h3><p>Lorem Ipsum is simply dummy text of the printing and typesetting industry.</p><a class="read-more" href="#">Read More</a>
  </article>
  <article class="abs theme-card" style="left:90px;top:982px">
    <div class="theme-photo" role="img" aria-label="Photo of children feeding a horse at a farm fence" style="background:linear-gradient(160deg,#6d7a5a,#3d4d33 55%,#7d8f5a)"></div>
    <h3>Explore Animals</h3><p>Lorem Ipsum is simply dummy text of the printing and typesetting industry.</p><a class="read-more" href="#">Read More</a>
  </article>
  <article class="abs theme-card" style="left:324px;top:982px">
    <div class="theme-photo" role="img" aria-label="Photo of a child beside a giant tennis ball sculpture" style="background:radial-gradient(circle at 50% 50%,#d6e04a,#9bb43a 55%,#2b6fa8)"></div>
    <h3>Explore Fitness</h3><p>Lorem Ipsum is simply dummy text of the printing and typesetting industry.</p><a class="read-more" href="#">Read More</a>
  </article>
  <article class="abs theme-card" style="left:555px;top:982px">
    <div class="theme-photo" role="img" aria-label="Black and white photo of a child on playground equipment" style="background:linear-gradient(160deg,#2a2a2a,#8a8a8a 55%,#cfcfcf)"></div>
    <h3>Explore Playgrounds</h3><p>Lorem Ipsum is simply dummy text of the printing and typesetting industry.</p><a class="read-more" href="#">Read More</a>
  </article>

  <aside class="abs newsletter">
    <h2>Newsletter Sign up</h2>
    <p>Lorem Ipsum is simply dummy text of the printing and typesetting industry.</p>
    <div class="field"></div>
    <div class="submit">Submit</div>
  </aside>
  <div class="abs promo" role="img" aria-label="Colourful poster listing types of persuasive text"></div>

  <div class="abs col-head small" style="left:90px;width:445px;background:var(--orange-dark)">
    <span class="ring"><svg width="16" height="14" viewBox="0 0 16 14"><path d="M0 7h12M8 2l5 5-5 5" stroke="#e07412" stroke-width="2.6" fill="none"/></svg></span>Lanternbugs selections of the month</div>
  <div class="abs col-head" style="left:535px;width:287px;background:var(--orange)">
    <span class="ring"><svg width="16" height="14" viewBox="0 0 16 14"><path d="M0 7h12M8 2l5 5-5 5" stroke="#f7941d" stroke-width="2.6" fill="none"/></svg></span>Suggested Post Today</div>
  <div class="abs col-head" style="left:823px;width:285px;background:var(--blue)">
    <span class="ring"><svg width="16" height="14" viewBox="0 0 16 14"><path d="M0 7h12M8 2l5 5-5 5" stroke="#0d4ea6" stroke-width="2.6" fill="none"/></svg></span>Featured Adventure</div>

  <article class="abs suggest-item" style="top:1391px">
    <div class="thumb" role="img" aria-label="Photo of two children running on a grassy hill" style="background:linear-gradient(160deg,#8fb6d8,#6e9a4a 55%,#c9a76a)"></div>
    <div class="body"><h4>Concert of classical music and stories told</h4><p>Lorem Ipsum has been the industry's standard dummy text ever since the 1500s, when an unknown printer took</p><a class="read-more" href="#">Read More</a></div>
  </article>
  <article class="abs suggest-item" style="top:1555px">
    <div class="thumb" role="img" aria-label="Photo of a child playing with a ship's wheel" style="background:linear-gradient(160deg,#e8dccb,#c49a6a 55%,#8a3a2a)"></div>
    <div class="body"><h4>Concert of classical music and stories told</h4><p>Lorem Ipsum has been the industry's standard dummy text ever since the 1500s, when an unknown printer took</p><a class="read-more" href="#">Read More</a></div>
  </article>
  <article class="abs suggest-item" style="top:1711px">
    <div class="thumb" role="img" aria-label="Photo of children in colourful costumes dancing" style="background:linear-gradient(160deg,#e6a3c0,#c05a8a 50%,#e8c26a)"></div>
    <div class="body"><h4>Concert of classical music and stories told</h4><p>Lorem Ipsum has been the industry's standard dummy text ever since the 1500s, when an unknown printer took</p><a class="read-more" href="#">Read More</a></div>
  </article>
  <article class="abs suggest-item" style="top:1874px">
    <div class="thumb" role="img" aria-label="Photo of children in colourful costumes dancing" style="background:linear-gradient(160deg,#e6a3c0,#c05a8a 50%,#e8c26a)"></div>
    <div class="body"><h4>Concert of classical music and stories told</h4><p>Lorem Ipsum has been the industry's standard dummy text ever since the 1500s, when an unknown printer took</p><a class="read-more" href="#">Read More</a></div>
  </article>

  <article class="abs post-card">
    <div class="photo" role="img" aria-label="Photo of a child holding a ship's wheel among antique toys" style="background:linear-gradient(180deg,#efe7dc,#d9c3a5 60%,#8a3a2a)"></div>
    <h4>Concert of classical music</h4>
    <p>Lorem Ipsum has been the industry's standard dummy text ever</p>
    <div class="btn">Read More</div>
  </article>

  <article class="abs feature-item" style="top:1396px"><div class="thumb" role="img" aria-label="Photo of two children running outdoors" style="background:linear-gradient(160deg,#8fb6d8,#6e9a4a 55%,#c9a76a)"></div><p><b>Lorem Ipsum has been the industry's</b> dummy text ever since the 1500s, when an unknown printer took</p></article>
  <article class="abs feature-item" style="top:1502px"><div class="thumb" role="img" aria-label="Photo of children dancing in costumes" style="background:linear-gradient(160deg,#e6a3c0,#c05a8a 50%,#5a6ab0)"></div><p><b>Lorem Ipsum has been the industry's</b> dummy text ever since the 1500s, when an unknown printer took</p></article>
  <article class="abs feature-item" style="top:1608px"><div class="thumb" role="img" aria-label="Photo of a child on a colourful climbing frame" style="background:linear-gradient(160deg,#d84a4a,#3aa0c0 50%,#e8c24a)"></div><p><b>Lorem Ipsum has been the industry's</b> dummy text ever since the 1500s, when an unknown printer took</p></article>
  <article class="abs feature-item" style="top:1714px"><div class="thumb" role="img" aria-label="Photo of a child in a yellow kayak on water" style="background:linear-gradient(160deg,#4a6a8a,#e8c23a 55%,#2a4a6a)"></div><p><b>Lorem Ipsum has been the industry's</b> dummy text ever since the 1500s, when an unknown printer took</p></article>
  <article class="abs feature-item" style="top:1820px"><div class="thumb" role="img" aria-label="Photo of a child playing in a garden" style="background:linear-gradient(160deg,#9ac07a,#4a7a3a 55%,#c8b89a)"></div><p><b>Lorem Ipsum has been the industry's</b> dummy text ever since the 1500s, when an unknown printer took</p></article>
</main>

<footer>
  <div class="abs footer"></div>
  <h3 class="abs f-title" style="left:61px">Contact us</h3><div class="abs f-rule" style="left:61px"></div>
  <h3 class="abs f-title" style="left:375px">Our Services</h3><div class="abs f-rule" style="left:375px"></div>
  <h3 class="abs f-title" style="left:627px">Store Hours</h3><div class="abs f-rule" style="left:627px"></div>
  <h3 class="abs f-title" style="left:869px">Our Location</h3><div class="abs f-rule" style="left:869px"></div>

  <div class="abs f-line" style="left:61px;top:2220px">
    <svg width="18" height="18" viewBox="0 0 18 18"><path d="M4 1l3 4-2 2c1 2 3 4 5 5l2-2 4 3-2 3C8 16 2 10 1 4z" fill="#fff"/></svg>9612 045 830</div>
  <div class="abs f-line" style="left:61px;top:2250px">
    <svg width="18" height="13" viewBox="0 0 18 13"><rect x="0.5" y="0.5" width="17" height="12" fill="none" stroke="#fff"/><path d="M1 1l8 6 8-6" stroke="#fff" fill="none"/></svg>contact@lanternbugs.com.au</div>
  <span class="abs social" style="left:60px"></span>
  <span class="abs social" style="left:96px"></span>
  <span class="abs social" style="left:132px"></span>
  <span class="abs social" style="left:172px"></span>

  <ul class="abs f-list bullets" style="left:375px;top:2209px">
    <li>Home</li><li>About Us</li><li>News</li><li>Free Tests</li><li>Gumleaf Stores</li><li>Community</li><li>Courses</li>
  </ul>
  <ul class="abs f-list" style="left:627px;top:2209px">
    <li>Monday:10am - 8pm</li><li>Tuesday:10am - 7pm</li><li>Wednesday:10am - 8pm</li><li>Thursday: 10am - 8pm</li><li>Friday:10am - 8pm</li><li>Saturday:10am - 7pm</li>
  </ul>
  <div class="abs map" role="img" aria-label="Street map showing the store location with a red marker"></div>

  <div class="abs footer-bar">© 2016 Copyright Lanternbugs. All Right Reserved</div>
</footer>

</body>
</html>
```